School Signage

I am wanting designs for signs completed that prompt students of the school requirements for hats, preparation and play.

I've uploaded rough examples of what we're after, but we would like them stylised and better than the example, including:
- A stylised logo/graphic for the 'Wallumba 1, 2, 3'
- Clear, crisp signage for the words.
- Graphics that reinforce the message of the sign.

We're after three signs:
- One that will be located on the oval to prompt hat use.
- One that will be near the entry prompting the morning routine (please make this one landscape with instructions for 'on time' on one side, and 'late' on the other).
- One that will be located within the school prompting readiness for class.

```html
<!DOCTYPE html>
<html lang="en">
<head>
<meta charset="utf-8">
<title>Wallumba 1, 2, 3 – School Signage</title>
<link rel="stylesheet" href="https://fonts.googleapis.com/css2?family=Baloo+2:wght@600;700;800&family=Ubuntu:wght@400;500&display=swap">
<style>
  :root{
    --stage:#3b3b3b;
    --paper:#ffffff;
    --green-deep:#0b6b3a;
    --green-mid:#009a4c;
    --green-band:#17793f;
    --green-soft:#5d9a52;
    --green-lime:#8dc63f;
    --green-sage:#6e9a73;
    --gold:#c8ad61;
    --ink:#1d1d1b;
    --ink-green:#0f7a3a;
  }
  *{box-sizing:border-box;margin:0;padding:0}
  html,body{width:1200px;height:630px;overflow:hidden;background:var(--stage)}
  .canvas{position:relative;width:1200px;height:630px;background:var(--stage);font-family:"Ubuntu",sans-serif;color:var(--ink)}
  .sign{position:absolute;top:134px;height:362px;background:var(--paper);overflow:hidden;box-shadow:0 6px 14px rgba(0,0,0,.35)}
  .sign--hats{left:53px;width:241px}
  .sign--class{left:329px;width:242px}
  .sign--routine{left:604px;width:543px;background:linear-gradient(180deg,#fff 0,#fff 135px,#c9dcc2 240px,#6fa660 330px,#4e9246 362px)}
  .wave{position:absolute;top:0;left:0;width:100%}
  .heading{position:absolute;left:0;width:100%;text-align:center;font-family:"Baloo 2",sans-serif;font-weight:700;font-style:italic;color:var(--ink-green);line-height:1.05}
  .pill{position:absolute;background:var(--gold);border-radius:12px;font-family:"Ubuntu",sans-serif;font-weight:500;color:var(--ink);text-align:center;white-space:nowrap}
  .row{position:absolute;height:28px;border:2px solid var(--green-band);border-radius:5px;background:#fff;display:flex;align-items:center}
  .row__num{position:absolute;left:-22px;top:-10px;font-family:"Baloo 2",sans-serif;font-weight:800;font-size:38px;line-height:1;color:var(--green-band);text-shadow:-2px 2px 0 var(--green-lime)}
  .row__icon{width:16px;height:18px;border-radius:3px;background:var(--green-soft);opacity:.85;margin:0 10px 0 18px;flex:none}
  .row__label{font-size:17px;color:var(--ink);line-height:1;white-space:nowrap}
  .row--compact .row__icon{margin:0 8px 0 10px}
  .row--compact .row__label{font-size:15px}
  .row__note{display:block;font-size:7px;margin-top:1px}
  .crest{position:absolute;border-radius:50%;background:#fff;border:3px solid var(--green-band);display:flex;align-items:center;justify-content:center;font-family:"Ubuntu",sans-serif;font-weight:500;font-size:8px;color:var(--green-band)}
  .band{position:absolute;left:0;width:100%}
  .value{position:absolute;color:#fff;font-size:16px;white-space:nowrap}
  .routine-title{position:absolute;left:27px;top:25px;font-family:"Baloo 2",sans-serif;font-weight:800;font-style:italic;font-size:33px;line-height:1;color:var(--green-band);white-space:nowrap}
  .routine-pill{position:absolute;left:0;top:68px;width:232px;height:29px;background:var(--gold);border-radius:0 15px 15px 0;font-weight:500;font-size:20px;line-height:29px;padding-left:27px;white-space:nowrap}
  .col-head{position:absolute;top:107px;width:147px;height:27px;border:2px solid var(--green-band);border-radius:4px;text-align:center;font-size:19px;line-height:23px;color:var(--green-mid);background:#fff;white-space:nowrap}
  .divider{position:absolute;left:271px;top:123px;width:1px;height:157px;background:#555}
  .step{position:absolute;font-size:13px;line-height:14.5px;color:var(--ink);white-space:nowrap}
  .step-num{position:absolute;font-family:"Baloo 2",sans-serif;font-weight:800;font-size:50px;line-height:1;color:var(--green-band);text-shadow:-3px 3px 0 var(--green-lime)}
  .motto-art{position:absolute;left:76px;top:303px;width:120px;height:46px;border-radius:4px;background:linear-gradient(90deg,rgba(255,255,255,.25),rgba(255,255,255,.45))}
  .motto-rule{position:absolute;left:204px;top:304px;width:1px;height:44px;background:#3d3d3d}
  .tagline{position:absolute;left:262px;top:314px;width:281px;height:28px;background:var(--gold);font-weight:500;font-size:19px;line-height:28px;padding-left:30px;white-space:nowrap}
</style>
</head>
<body>
<main class="canvas">

  <!-- Hat sign -->
  <section class="sign sign--hats">
    <svg class="wave" viewBox="0 0 241 80" height="80" aria-hidden="true">
      <path d="M0 0H241V36C215 30 200 58 176 52C160 48 150 40 130 50C110 60 100 44 84 40C70 37 66 60 50 72C40 78 30 70 28 56C24 40 12 60 0 58Z" fill="var(--green-sage)"/>
      <path d="M120 0H241V55C225 48 210 62 190 58C175 55 170 45 150 50C140 52 125 45 120 30Z" fill="var(--green-lime)"/>
      <path d="M0 0H241V40C220 34 205 52 185 46C165 40 150 30 132 42C118 52 106 36 94 30C80 24 70 46 52 46C36 46 20 52 0 58Z" fill="var(--green-mid)"/>
      <path d="M0 0H140C152 12 148 28 130 30C112 32 100 22 86 28C70 34 56 26 44 34C30 42 14 40 0 44Z" fill="var(--green-deep)"/>
    </svg>
    <h2 class="heading" style="top:76px;font-size:15px">We wear Hats at<br>Wallumba when outdoors...</h2>
    <div class="pill" style="left:50px;top:117px;width:140px;height:19px;font-size:13px;line-height:19px">Wallumba 1, 2, 3</div>
    <div class="row" style="left:67px;top:149px;width:121px"><span class="row__num">1</span><span class="row__icon" role="img" aria-label="Walking figure icon"></span><span class="row__label">Walking</span></div>
    <div class="row" style="left:67px;top:185px;width:121px"><span class="row__num">2</span><span class="row__icon" role="img" aria-label="Seated figure icon"></span><span class="row__label">Sitting</span></div>
    <div class="row" style="left:67px;top:221px;width:121px"><span class="row__num">3</span><span class="row__icon" role="img" aria-label="Figure kicking a ball icon"></span><span class="row__label">Playing</span></div>
    <div class="band" style="top:283px;height:79px;background:linear-gradient(180deg,var(--green-band) 0,var(--green-band) 22px,#5b9a4e 22px,#9cc48f 50px,#fff 79px)"></div>
    <div class="crest" style="left:62px;top:269px;width:50px;height:50px">Wallumba</div>
    <span class="value" style="left:124px;top:284px">Integrity</span>
  </section>

  <!-- Ready for class sign -->
  <section class="sign sign--class">
    <svg class="wave" viewBox="0 0 241 80" height="80" aria-hidden="true">
      <path d="M0 0H241V36C215 30 200 58 176 52C160 48 150 40 130 50C110 60 100 44 84 40C70 37 66 60 50 72C40 78 30 70 28 56C24 40 12 60 0 58Z" fill="var(--green-sage)"/>
      <path d="M120 0H241V55C225 48 210 62 190 58C175 55 170 45 150 50C140 52 125 45 120 30Z" fill="var(--green-lime)"/>
      <path d="M0 0H241V40C220 34 205 52 185 46C165 40 150 30 132 42C118 52 106 36 94 30C80 24 70 46 52 46C36 46 20 52 0 58Z" fill="var(--green-mid)"/>
      <path d="M0 0H140C152 12 148 28 130 30C112 32 100 22 86 28C70 34 56 26 44 34C30 42 14 40 0 44Z" fill="var(--green-deep)"/>
    </svg>
    <h2 class="heading" style="top:82px;font-size:19px">Are you ready for class?</h2>
    <div class="pill" style="left:51px;top:109px;width:140px;height:19px;font-size:13px;line-height:19px">Wallumba 1, 2, 3</div>
    <div class="row row--compact" style="left:36px;top:145px;width:183px"><span class="row__num">1</span><span class="row__icon" role="img" aria-label="Laptop icon"></span><span class="row__label">Laptop/ Workbook</span></div>
    <div class="row row--compact" style="left:36px;top:180px;width:183px"><span class="row__num">2</span><span class="row__icon" role="img" aria-label="Padlock icon"></span><span class="row__label">Phone in Pouchlok</span></div>
    <div class="row row--compact" style="left:36px;top:214px;width:183px"><span class="row__num">3</span><span class="row__icon" role="img" aria-label="Cap icon"></span><span class="row__label">Correct Uniform<span class="row__note">(Including Hat)</span></span></div>
    <svg class="band" style="top:262px" viewBox="0 0 242 100" height="100" preserveAspectRatio="none" aria-hidden="true">
      <defs><linearGradient id="classFoot" x1="0" y1="0" x2="0" y2="1"><stop offset="0" stop-color="#3f8d45"/><stop offset=".6" stop-color="#7fb272"/><stop offset="1" stop-color="#fff"/></linearGradient></defs>
      <path d="M0 26C40 18 70 36 100 28C130 20 160 40 190 20C210 6 230 0 242 2V100H0Z" fill="var(--green-lime)"/>
      <path d="M0 30C40 22 70 40 100 32C130 24 160 44 190 24C210 10 230 4 242 6V100H0Z" fill="url(#classFoot)"/>
    </svg>
    <div class="crest" style="left:96px;top:257px;width:50px;height:50px">Wallumba</div>
    <span class="value" style="left:0;width:100%;text-align:center;top:311px;font-size:17px">Curiosity &amp; Drive</span>
    <span class="value" style="left:0;width:100%;text-align:center;top:334px;font-size:10px;color:var(--ink)">Wallumba Learner Values</span>
  </section>

  <!-- Morning routine sign -->
  <section class="sign sign--routine">
    <svg class="wave" style="left:263px;width:280px" viewBox="0 0 280 70" height="70" aria-hidden="true">
      <path d="M0 0H280V60C262 56 252 40 234 32C214 24 196 38 176 30C160 24 156 6 140 6C124 6 114 30 96 30C78 30 70 10 50 8C30 6 14 4 0 0Z" fill="var(--green-lime)"/>
      <path d="M0 0H280V50C262 46 250 34 230 28C212 22 196 34 176 26C160 20 154 2 138 4C122 6 110 24 94 24C74 24 68 2 44 2Z" fill="var(--green-sage)"/>
      <path d="M120 0H280V46C262 44 250 30 230 22C212 16 196 24 178 16C164 10 150 2 120 0Z" fill="var(--green-mid)"/>
    </svg>
    <h1 class="routine-title">Morning Routine</h1>
    <div class="routine-pill">The Wallumba 1, 2, 3</div>

    <div class="col-head" style="left:41px">On Time:</div>
    <div class="col-head" style="left:304px">Running Late:</div>
    <div class="divider"></div>

    <span class="step-num" style="left:44px;top:137px">1</span>
    <p class="step" style="left:91px;top:152px">Arrive before 8:30am</p>
    <span class="step-num" style="left:44px;top:187px">2</span>
    <p class="step" style="left:91px;top:198px">Drop bag at locker and<br>collect learning materials</p>
    <span class="step-num" style="left:44px;top:240px">3</span>
    <p class="step" style="left:91px;top:243px">Arrive at Home Group /<br>House Assembly<br>before 8:40 AM</p>

    <span class="step-num" style="left:307px;top:137px">1</span>
    <p class="step" style="left:356px;top:152px">Arrive before 8:30 AM</p>
    <span class="step-num" style="left:307px;top:187px">2</span>
    <p class="step" style="left:356px;top:198px">Drop bag at locker and<br>collect learning materials</p>
    <span class="step-num" style="left:307px;top:240px">3</span>
    <p class="step" style="left:356px;top:243px">Arrive at Home Group /<br>House Assembly<br>before 8:40 AM</p>

    <div class="motto-art" role="img" aria-label="Hand-lettered motto: Early is on time, on time is late"></div>
    <div class="motto-rule"></div>
    <div class="tagline">Exceed Your Expectations</div>
    <div class="crest" style="left:222px;top:299px;width:54px;height:54px">Wallumba</div>
  </section>

</main>
</body>
</html>
```